improvement on my landing page

We are a fansite platform similar to velbrook.com, quindleo.com , tarvimu.com and gorbelix.com. We are aiming to disrupt this space by a much cheaper and advanced platform to help influencers monetise across different tools.

current lander is https://plumvarra.com/

Looking for a modern, clean, feminine , pink. Current style and other competitors list given feel old and this needs to highlight its a cutting edge product replacing them. Designs I like are www.brisko.app for example.

I need a few elaborations from current site on price differences of competitors, icons and more details on features and several other new sections added. Need a form to capture email , name and phone as this is a coming soon page. Can change later as a signup

attached document is how thee site looks, so need to keep the identity

Target Market(s)

influence's, adult

Font styles to use
Sans Serif

Colors
eea4c8
fefafc
ecdaeb

Requirements
Nice to have
• infographics

```html
<!DOCTYPE html>
<html lang="en">
<head>
<meta charset="utf-8">
<title>Plumvarra – Keep 90% of your earnings</title>
<link rel="stylesheet" href="https://fonts.googleapis.com/css2?family=Jost:wght@400;500;600;700&display=swap">
<style>
:root{
  --pink:#e03d8c;
  --pink-soft:#f57bb8;
  --pink-pale:#eea4c8;
  --lavender:#ede1fb;
  --ink:#2c2c2c;
  --muted:#555;
  --white:#ffffff;
  --off:#fefafc;
}
*{box-sizing:border-box;margin:0;padding:0}
html,body{width:752px;height:1200px;overflow:hidden}
body{position:relative;font-family:'Jost',sans-serif;background:var(--off);color:var(--ink)}
.abs{position:absolute}

/* hero */
.hero{left:0;top:0;width:752px;height:311px;overflow:hidden}
.hero-photo{position:absolute;inset:0;background:
  radial-gradient(ellipse 160px 200px at 400px 180px,#d8a98f 0%,rgba(216,169,143,0) 70%),
  linear-gradient(90deg,#4a3a2c 0%,#6b5441 35%,#8a6c52 55%,#6a5a48 80%,#4d4a3a 100%)}
.hero-shade{position:absolute;inset:0;background:linear-gradient(90deg,rgba(0,0,0,.35),rgba(0,0,0,0) 60%)}
.hero-brand{left:46px;top:28px;font-size:32px;font-weight:500;letter-spacing:2px;color:var(--white)}
.hero-head{left:46px;top:128px;width:300px;text-align:center;font-size:18.5px;font-weight:500;letter-spacing:1.8px;line-height:28px;color:var(--white)}
.hero-copy{left:46px;top:204px;width:250px;text-align:center;font-size:8.6px;line-height:14px;color:var(--white)}
.hero-copy b{color:var(--pink-pale);font-weight:600}
.btn{display:flex;align-items:center;justify-content:center;border-radius:14px;font-weight:600;color:var(--white)}
.btn-start{left:47px;top:251px;width:114px;height:26px;background:var(--pink);font-size:8.5px}
.btn-more{left:165px;top:251px;width:114px;height:26px;border:1px solid var(--white);font-size:8.5px;font-weight:500}

/* why */
.why-brand{left:0;width:752px;top:348px;text-align:center;font-size:32px;font-weight:500;letter-spacing:2px;color:var(--ink)}
.why-title{left:0;width:752px;top:406px;text-align:center;font-size:14px;font-weight:500;letter-spacing:1.3px}
.why-title span{color:var(--pink)}
.note{border-radius:3px;color:var(--white);font-size:8px;line-height:12.7px;font-weight:500;letter-spacing:.2px}
.note-main{left:107px;top:451px;width:451px;height:101px;background:var(--pink);padding:25px 18px 0 19px}
.note-more{left:297px;top:532px;width:348px;height:102px;background:var(--pink-soft);padding:42px 18px 0 19px}

/* features */
.features{left:0;top:680px;width:752px;height:259px;background:var(--lavender)}
.feature{top:743px;width:170px;text-align:center}
.feature svg{display:block;margin:0 auto}
.feature h3{margin-top:7px;font-size:9.5px;font-weight:500;letter-spacing:.9px;color:var(--ink)}
.feature p{margin:5px auto 0;width:112px;font-size:7.4px;line-height:11.5px;color:var(--muted)}
.dot{top:921px;width:6px;height:6px;border-radius:50%;background:var(--white)}
.dot.on{background:var(--pink)}

/* pricing + signup */
.city{left:0;top:939px;width:752px;height:261px;background:
  linear-gradient(180deg,rgba(46,110,160,.95) 0%,rgba(78,120,150,.9) 35%,rgba(140,110,120,.85) 70%,rgba(70,60,80,.95) 100%)}
.label{font-weight:700;color:var(--white);letter-spacing:.5px}
.fees-title{left:81px;top:971px;width:141px;text-align:center;font-size:12px}
.our-title{left:234px;top:973px;width:140px;text-align:center;font-size:12px}
.glass{background:rgba(255,255,255,.2);border-radius:4px}
.card-rivals{left:81px;top:995px;width:141px;height:140px;background:rgba(190,90,170,.45)}
.rival{left:100px;width:120px;display:flex;align-items:center;gap:10px;color:var(--white)}
.rival i{width:36px;height:36px;border-radius:50%;flex:none;display:flex;align-items:center;justify-content:center;font-style:normal;font-size:6.5px;font-weight:600}
.rival b{font-size:11px;font-weight:700}
.card-ours{left:234px;top:995px;width:140px;height:140px}
.ours-name{left:234px;top:1002px;width:140px;text-align:center;font-size:15px}
.ours-sub{left:234px;top:1032px;width:140px;text-align:center;font-size:11.5px}
.ours-rate{left:234px;top:1049px;width:140px;text-align:center;font-size:31px;font-weight:700;color:var(--white)}
.btn-ours{left:247px;top:1101px;width:114px;height:26px;background:var(--pink);font-size:8.5px}
.divider{left:445px;top:990px;width:1px;height:164px;background:rgba(255,255,255,.35)}
.form-title{left:470px;top:968px;width:233px;text-align:center;font-size:12px}
.form-sub{left:470px;top:984px;width:233px;text-align:center;font-size:7.8px;color:var(--white)}
.signup{left:516px;top:1002px;width:147px;height:148px;background:rgba(226,70,150,.85);border-radius:4px}
.field{left:530px;width:119px;height:17px;border-radius:3px;background:rgba(255,255,255,.28);color:var(--white);font-size:6.3px;padding:5px 8px}
.btn-register{left:536px;top:1119px;width:113px;height:25px;border:1px solid var(--white);background:transparent;font-size:8.5px}
.footer{left:0;top:1181px;width:752px;text-align:center;font-size:6.5px;color:var(--white)}
</style>
</head>
<body>

<section class="hero abs">
  <div class="hero-photo" role="img" aria-label="Photo of a smiling creator on a sofa working on a laptop in a warm cafe"></div>
  <div class="hero-shade"></div>
</section>
<div class="hero-brand abs">PLUMVARRA</div>
<h1 class="hero-head abs">KEEP 90% OF YOUR EARNINGS<br>NO HIDDEN FEES.</h1>
<p class="hero-copy abs">Make more with added revenue streams and features for <b>FREE</b>.<br>Maximise you're your fanbase profits with Plumvarra.</p>
<a class="btn btn-start abs">GET STARTED</a>
<a class="btn btn-more abs">Learn More</a>

<div class="why-brand abs">PLUMVARRA</div>
<h2 class="why-title abs">WHY CHOOSE <span>US</span>?</h2>
<div class="note note-main abs">Plumvarra was developed to democratise the fan platform space.As entrepreurs ourselves we don't see why you should you be handing over a high percentageof your hard earned profits to platforms with mediocre features and services. Receive 90% of your earnings, with no hidden fees or extras<br>AND with fastest payouts.</div>
<div class="note note-more abs">Monetize with monthly subscriptions through private profile feeds<br>and premium social media accounts. Private messaging and tipping,<br>premium videos and much more. Start earning more and keeping your profits.</div>

<section class="features abs"></section>

<div class="feature abs" style="left:40px">
  <svg width="90" height="90" viewBox="0 0 90 90" fill="none" stroke="#e03d8c">
    <path d="M55 3 A42 42 0 1 1 22 81" stroke-width="2.5"/><path d="M35 4 A42 42 0 0 0 5 55" stroke-width="1.5"/>
    <g stroke-width="1.3"><rect x="27" y="28" width="20" height="4"/><rect x="27" y="60" width="20" height="4"/><path d="M29 32 Q37 46 29 60 M45 32 Q37 46 45 60"/><circle cx="56" cy="46" r="7"/><path d="M56 42v8 M53 44h5 M53 48h5"/><rect x="51" y="54" width="14" height="10"/></g>
  </svg>
  <h3>FASTEST PAYOUTS</h3><p>Get your money in less than 7 days</p>
</div>
<div class="feature abs" style="left:195px">
  <svg width="90" height="90" viewBox="0 0 90 90" fill="none" stroke="#e03d8c">
    <path d="M55 3 A42 42 0 1 1 22 81" stroke-width="2.5"/><path d="M35 4 A42 42 0 0 0 5 55" stroke-width="1.5"/>
    <g stroke-width="1.3"><circle cx="42" cy="50" r="14"/><ellipse cx="42" cy="50" rx="6" ry="14"/><path d="M28 50h28 M30 43h24 M30 57h24"/><path d="M33 33l10-6 8 5 11-7"/><circle cx="62" cy="25" r="2"/><rect x="54" y="56" width="10" height="8"/><path d="M56 56v-3a3 3 0 0 1 6 0v3"/></g>
  </svg>
  <h3>GEO BLOCKING</h3><p>Hide your content from specific countries</p>
</div>
<div class="feature abs" style="left:360px">
  <svg width="90" height="90" viewBox="0 0 90 90" fill="none" stroke="#e03d8c">
    <path d="M55 3 A42 42 0 1 1 22 81" stroke-width="2.5"/><path d="M35 4 A42 42 0 0 0 5 55" stroke-width="1.5"/>
    <g stroke-width="1.3"><rect x="31" y="26" width="28" height="38"/><path d="M45 32l10 4v8c0 7-5 11-10 13-5-2-10-6-10-13v-8z"/><path d="M49 42a5 5 0 1 0 0 6"/></g>
  </svg>
  <h3>COPYRIGHT PROTECTION</h3><p>You own your content. Take it down whenever you want</p>
</div>
<div class="feature abs" style="left:524px">
  <svg width="90" height="90" viewBox="0 0 90 90" fill="none" stroke="#e03d8c">
    <path d="M55 3 A42 42 0 1 1 22 81" stroke-width="2.5"/><path d="M35 4 A42 42 0 0 0 5 55" stroke-width="1.5"/>
    <g stroke-width="1.3"><rect x="25" y="30" width="12" height="24"/><rect x="39" y="26" width="14" height="30"/><rect x="55" y="30" width="12" height="24"/><path d="M43 34h6 M43 40h6 M43 46h6 M28 36h6 M28 42h6 M58 36h6 M58 42h6"/><path d="M45 50v12h6v-6"/></g>
  </svg>
  <h3>CUSTOMIZABLE SUBSCRIPTIONS</h3><p>Build your own subscription plan to fit your busines</p>
</div>
<span class="dot on abs" style="left:357px"></span>
<span class="dot abs" style="left:367px"></span>
<span class="dot abs" style="left:378px"></span>

<section class="city abs" role="img" aria-label="Blurred aerial photo of a city skyline at dusk"></section>
<div class="fees-title label abs">COMPETITOR FEES</div>
<div class="card-rivals abs"></div>
<div class="rival abs" style="top:1008px"><i style="background:#f2694b">Velbrook</i><b>20 %</b></div>
<div class="rival abs" style="top:1057px"><i style="background:#1ea8e8">Tarvimu</i><b>42.5 %</b></div>
<div class="rival abs" style="top:1100px"><i style="background:#7a5bc9">Gorbelix</i><b>25-35 %</b></div>

<div class="our-title label abs">OUR FEES</div>
<div class="card-ours glass abs"></div>
<div class="ours-name label abs">PLUMVARRA</div>
<div class="ours-sub label abs">OFFER YOU</div>
<div class="ours-rate abs">10%</div>
<a class="btn btn-ours abs">GET STARTED</a>

<div class="divider abs"></div>
<div class="form-title label abs">Create Your FREE Account</div>
<div class="form-sub abs">It only takes a few seconds. No credit card required.</div>
<form class="signup abs"></form>
<div class="field abs" style="top:1011px">Username</div>
<div class="field abs" style="top:1038px">Email</div>
<div class="field abs" style="top:1065px">Password</div>
<div class="field abs" style="top:1092px">Repeat Password</div>
<a class="btn btn-register abs">REGISTER</a>

<div class="footer abs">PrivacyTerms &amp; Conditions</div>
</body>
</html>
```